Locksmith Business Cards

My father-in-law is in need of new business cards for his locksmith business and I need to impress him. Kindly help me out!

You can see the previous business card attached. It is a family run business in North Wales.

No individual names on the cards.

Key Things to Feature:
- The words "Prompt", "Local", "Reliable" (as you can see under the logo on the website)
- 24h Emergency Service
- Covering All of North Wales, the Wirral and Chester
- The color blue
- A key or a lock would be interesting (similar to the ones that come up when you google locksmith business card)

Optional (only if design includes bullet points, like the example below):
https://imgvaultcdnx.net/design_img/318264/57190/57190_2749031_318264_image.jpg
- Residential / Commercial / Automotive
- Alarms & Cameras
- Key Cutting & Safes

https://www.bryncoed-locksmiths-demo.co.uk/

Locksmith

01632 960 418
07700 900 362
bryncoedlocksmiths@mailvalex.com
Bryncoed Locksmiths, Hafod Barn, 4 Pennant Rd., Llandudno LL39 7QZ
www.bryncoed-locksmiths-demo.co.uk

• - The words "Prompt", "Local", "Reliable" (as you can see under the logo on the website)
• - 24h Emergency Service
• - Covering All of North Wales, the Wirral and Chester
• - A key or a lock would be interesting (similar to the ones that come up when you google locksmith business card)

```html
<!DOCTYPE html>
<html lang="en">
<head>
<meta charset="utf-8">
<title>Bryncoed Locksmiths – Business Card</title>
<link rel="stylesheet" href="https://fonts.googleapis.com/css2?family=Arimo:wght@400;700&display=swap">
<style>
  :root {
    --ink: #11151e;
    --blue: #1a5cff;
    --white: #ffffff;
    --paper: #ffffff;
  }
  * { margin: 0; padding: 0; box-sizing: border-box; }
  html, body {
    width: 1200px; height: 678px; overflow: hidden;
    background: var(--ink);
    font-family: "Arimo", Arial, sans-serif;
  }
  .card {
    position: relative; width: 1200px; height: 678px;
    background: var(--ink); overflow: hidden;
  }
  .brand-panel {
    position: absolute; left: 0; top: 0; width: 379px; height: 678px;
    background: var(--paper);
  }
  .accent-bar {
    position: absolute; left: 379px; top: 0; width: 16px; height: 678px;
    background: var(--blue);
  }
  .brand {
    position: absolute; left: 0; top: 0; width: 379px; height: 359px;
    display: flex; flex-direction: column; align-items: center; justify-content: center;
    gap: 22px;
  }
  .brand-name {
    display: flex; align-items: center; gap: 14px;
    color: var(--blue); font-weight: 700; font-size: 29px;
    line-height: 1.1; letter-spacing: 0.5px; text-transform: uppercase;
  }
  .brand-mark { flex: none; }
  .brand-est {
    color: var(--blue); font-weight: 400; font-size: 17px;
    letter-spacing: 3px;
  }
  .values { position: absolute; left: 0; top: 0; }
  .value {
    position: absolute; left: 0; width: 395px; height: 75px;
    background: var(--ink);
    display: flex; align-items: center; justify-content: center;
    color: var(--blue); font-weight: 700; font-size: 42px; letter-spacing: 4px;
  }
  .value--prompt { top: 359px; }
  .value--local { top: 458px; }
  .value--reliable { top: 558px; }
  .info {
    position: absolute; left: 395px; top: 0; width: 805px; height: 678px;
    color: var(--white); font-weight: 700;
  }
  .headline {
    position: absolute; left: 0; width: 805px; text-align: center;
    letter-spacing: 4.5px;
  }
  .headline--main { top: 56px; font-size: 44px; }
  .headline--sub { top: 132px; font-size: 40px; }
  .services {
    position: absolute; left: 64px; top: 256px; list-style: none;
  }
  .service {
    display: flex; align-items: center; gap: 22px;
    height: 70px; font-size: 26px; letter-spacing: 3.4px;
  }
  .service::before {
    content: ""; width: 18px; height: 18px; border-radius: 50%;
    background: var(--blue); flex: none;
  }
  .emergency {
    position: absolute; left: 0; top: 518px; width: 805px; text-align: center;
    font-size: 37px; letter-spacing: 4.5px;
  }
  .coverage {
    position: absolute; left: 0; top: 581px; width: 805px; text-align: center;
    font-size: 22px; letter-spacing: 3px;
  }
</style>
</head>
<body>
<main class="card">
  <section class="brand-panel">
    <div class="brand">
      <div class="brand-name">
        <svg class="brand-mark" width="40" height="40" viewBox="0 0 40 40" aria-hidden="true">
          <circle cx="20" cy="20" r="17" fill="none" stroke="#1a5cff" stroke-width="4"/>
        </svg>
        <span>Bryncoed<br>Locksmiths</span>
      </div>
      <p class="brand-est">Est Since 1989</p>
    </div>
  </section>
  <div class="accent-bar"></div>

  <div class="values">
    <p class="value value--prompt">PROMPT</p>
    <p class="value value--local">LOCAL</p>
    <p class="value value--reliable">RELIABLE</p>
  </div>

  <section class="info">
    <h1 class="headline headline--main">Your Local Locksmith</h1>
    <h2 class="headline headline--sub">No Job Too Small</h2>
    <ul class="services">
      <li class="service">Residential / Commercial / Automotive</li>
      <li class="service">Alarms &amp; Cameras</li>
      <li class="service">Key Cutting &amp; Safes</li>
    </ul>
    <p class="emergency">24h Emergency Service</p>
    <p class="coverage">Covering All of North Wales, the Wirral and Chester</p>
  </section>
</main>
</body>
</html>
```